Business Card Design Project

Im an electrician and my company name is Kestrel Electrical
My main work is installing Lighting and Power Points, Home Theater Systems, TVS, Phones and Data
Im looking a business card, something nice, clean, modern and not to cluttered
Im open to sugestions
I dont mind if the "Services" is on the back on the business card
colours black, grey, white or the blue colour of my logo are prefered but not compulsory
any questions just message me
and please make it so if i need to edit the writing can do it easy. maybe by making it a seperate layer ?
My Details are.
Name - Peter Halloran
Job Title - Licenced Electrician
Mobile - 027 583 2174
Email - peter@kestrelelectrical.co.nz
Web - www.kestrelelectrical.co.nz
Services
Residential / Commercial
Lighting & Power
Heating & Ventilation
Automation
Phone & Data
Home Cinema
Sound Systems
TV, Antenna & Satellite
Digital Upgrades

```html
<!DOCTYPE html>
<html lang="en">
<head>
<meta charset="utf-8">
<title>Kestrel Electrical – Business Card</title>
<link rel="stylesheet" href="https://fonts.googleapis.com/css2?family=Roboto:wght@400;500;700&family=Roboto+Condensed:wght@400;700&display=swap">
<style>
  :root {
    --teal: #0e9fb5;
    --slate: #56606a;
    --ink: #3a3f45;
    --card: #eef0f1;
    --card-shade: #e2e5e7;
    --backdrop: #d9d6d2;
    --white: #ffffff;
  }
  * { box-sizing: border-box; margin: 0; padding: 0; }
  html, body { width: 1200px; height: 880px; overflow: hidden; }
  body {
    background: var(--backdrop);
    font-family: "Roboto", Arial, sans-serif;
    position: relative;
  }
  .card {
    position: absolute;
    width: 540px;
    height: 310px;
    background: var(--card);
    box-shadow: 0 6px 18px rgba(0,0,0,0.18);
    overflow: hidden;
  }

  /* Front */
  .card--front { left: 60px; top: 460px; }
  .card--front .corner-band { position: absolute; inset: 0; }
  .brand {
    position: absolute;
    display: flex;
    align-items: center;
    gap: 10px;
  }
  .brand__square { width: 22px; height: 22px; background: var(--teal); flex: none; }
  .brand__name {
    font-weight: 700;
    color: var(--teal);
    letter-spacing: 0.06em;
    text-transform: uppercase;
    line-height: 1.1;
  }
  .card--front .brand { left: 40px; top: 30px; }
  .card--front .brand__name { font-size: 18px; }
  .holder { position: absolute; left: 48px; top: 112px; }
  .holder__name { font-size: 28px; font-weight: 700; color: var(--teal); }
  .holder__role { font-size: 18px; color: var(--ink); margin-top: 4px; }
  .contacts {
    position: absolute;
    left: 40px;
    top: 196px;
    border-collapse: collapse;
    font-size: 17px;
    color: var(--ink);
  }
  .contacts th { font-weight: 400; text-align: left; padding: 2px 8px 2px 0; }
  .contacts td { padding: 2px 0; }

  /* Back */
  .card--back { left: 600px; top: 130px; }
  .card--back .split { position: absolute; inset: 0; }
  .card--back .brand { left: 36px; top: 126px; gap: 12px; }
  .card--back .brand__square { background: var(--slate); width: 48px; height: 48px; }
  .card--back .brand__name { color: var(--slate); font-size: 22px; }
  .card--back .brand__line { display: block; }
  .services {
    position: absolute;
    right: 34px;
    top: 40px;
    text-align: right;
    font-family: "Roboto Condensed", "Arial Narrow", sans-serif;
    color: var(--white);
  }
  .services__title { font-size: 22px; font-weight: 700; margin-bottom: 10px; }
  .services__list { list-style: none; font-size: 16px; line-height: 1.3; }
</style>
</head>
<body>

  <section class="card card--front" aria-label="Business card front">
    <svg class="corner-band" width="540" height="310" viewBox="0 0 540 310" aria-hidden="true">
      <polygon points="540,140 540,310 380,310" fill="var(--card-shade)"/>
    </svg>
    <div class="brand">
      <span class="brand__square"></span>
      <span class="brand__name">Kestrel Electrical</span>
    </div>
    <div class="holder">
      <h1 class="holder__name">Peter Halloran</h1>
      <p class="holder__role">Licenced Electrician</p>
    </div>
    <table class="contacts">
      <tr><th>Mobile</th><td>: 027 583 2174</td></tr>
      <tr><th>Email</th><td>: peter@kestrelelectrical.co.nz</td></tr>
      <tr><th>Website</th><td>: www.kestrelelectrical.co.nz</td></tr>
    </table>
  </section>

  <section class="card card--back" aria-label="Business card back">
    <svg class="split" width="540" height="310" viewBox="0 0 540 310" aria-hidden="true">
      <polygon points="385,0 540,0 540,310 215,310" fill="var(--teal)"/>
    </svg>
    <div class="brand">
      <span class="brand__square"></span>
      <span class="brand__name">
        <span class="brand__line">Kestrel</span>
        <span class="brand__line">Electrical</span>
      </span>
    </div>
    <div class="services">
      <h2 class="services__title">SERVICES</h2>
      <ul class="services__list">
        <li>Lighting &amp; Power</li>
        <li>Heating &amp; Ventilation</li>
        <li>Automation</li>
        <li>Phone &amp; Data</li>
        <li>Home Cinema</li>
        <li>Sound Systems</li>
        <li>TV, Antenna &amp; Satellite</li>
        <li>Residential / Commercial</li>
        <li>Digital Upgrades</li>
      </ul>
    </div>
  </section>

</body>
</html>
```